Design a large parking banner – mandatory ticket validation in the shop

Banner Size:
548 cm (width) x 154 cm (height)
Note: The banner will be placed in a metal frame at our parking lot entrance, fully visible to every incoming truck driver. The message must be easy to read from a distance.
Goal of the Banner:
To inform all truck drivers that they must validate their entry ticket inside the shop, even if they are parking for a short time.
The message must be displayed in multiple languages for international drivers.
Mandatory Content:
Main message – in multiple languages (clearly separated or stacked):
Dutch (NL): Vergeet je ticket niet te valideren in de shop – verplicht, ook bij kort parkeren!
French (FR): N'oubliez pas de valider votre ticket à la boutique – obligatoire, même pour un court arrêt !
English (EN): Don't forget to validate your entry ticket in the shop – mandatory, even for short stops!
German (DE): Vergessen Sie nicht, Ihr Einfahrticket im Shop zu entwerten – Pflicht, auch bei kurzem Parken!
Polish (PL): Nie zapomnij zatwierdzić biletu w sklepie – obowiązkowe, nawet przy krótkim postoju!
Romanian (RO): Nu uitați să validați biletul în magazin – obligatoriu, chiar și pentru opriri scurte!
You can include more languages if space allows, but these are essential.
Opening Hours Block (in one section below):
Shop Opening Hours
Mon – Fri: 05:30 – 22:00
Sat & Sun: 08:00 – 22:00
Style & Branding:
The design must match the visual identity of Haulport 41Ter
Please refer to the attached photos of existing parking signage for guidance on colors, typography, and layout style
Our logo (attached) must be clearly visible and professionally integrated
Feel free to use icons or pictograms to visually support the message (e.g., ticket, truck, arrow)
Readability is key – large, bold text and high contrast colors that are visible from a distance
Target Audience:
International truck drivers – people who need fast, clear communication. Not everyone speaks the local language, so visual clarity and multilingual messaging are critical.
File Requirements:
Print-ready file (PDF or EPS) – 300 dpi at 1:10 scale
Include 5 cm bleed on all sides
Provide open source files if possible (AI or PSD)

```html
<!DOCTYPE html>
<html lang="en">
<head>
<meta charset="utf-8">
<title>Haulport 41Ter – Ticket Validation Banner</title>
<link href="https://fonts.googleapis.com/css2?family=Oswald:wght@500;600;700&family=Roboto+Condensed:ital,wght@1,700&family=Raleway:ital,wght@0,500;0,600;1,600&display=swap" rel="stylesheet">
<style>
  :root {
    --navy: #1d2a6c;
    --blue: #2a87d2;
    --red: #d8232a;
    --yellow: #f2e51b;
    --paper: #f4f5f7;
    --stage: #e3e6ea;
    --white: #ffffff;
  }
  * { box-sizing: border-box; margin: 0; padding: 0; }
  html, body { width: 1170px; height: 1200px; overflow: hidden; }
  body { background: var(--stage); position: relative; }

  .banner {
    --bg: var(--paper);
    --ink: var(--navy);
    --accent-blue: var(--blue);
    --accent-red: var(--red);
    --icon: var(--navy);
    position: absolute;
    left: 30px;
    width: 1110px;
    height: 324px;
    background: var(--bg);
    overflow: hidden;
    font-family: "Oswald", sans-serif;
    color: var(--ink);
  }
  .banner--light { top: 140px; }
  .banner--dark {
    top: 680px;
    --bg: var(--navy);
    --ink: var(--white);
    --accent-blue: var(--yellow);
    --accent-red: var(--yellow);
    --icon: var(--white);
    border-bottom: 4px solid var(--red);
  }

  /* header */
  .banner__header { position: relative; height: 100px; }
  .header-tab { position: absolute; top: 0; height: 90px; background: var(--blue); }
  .header-tab--left { left: 0; width: 420px; clip-path: polygon(0 0, 100% 0, 96% 100%, 0 100%); }
  .header-tab--right { right: 0; width: 430px; clip-path: polygon(0 0, 100% 0, 100% 100%, 5% 100%); }

  .steps {
    position: absolute; left: 26px; top: 24px;
    display: flex; align-items: center; gap: 10px;
    color: var(--icon);
  }
  .steps svg { display: block; }

  .brand {
    position: absolute; left: 555px; top: 24px;
    transform: translateX(-50%);
    font-family: "Oswald", sans-serif;
    font-weight: 700;
    font-size: 34px;
    line-height: 1;
    color: var(--navy);
    white-space: nowrap;
  }
  .banner--dark .brand { color: var(--white); }

  .hours {
    position: absolute; right: 22px; top: 20px;
    display: flex; align-items: center; gap: 7px;
    color: var(--navy);
  }
  .banner--dark .hours { color: var(--white); }
  .hours__shop {
    writing-mode: vertical-rl; transform: rotate(180deg);
    font-size: 16px; font-weight: 700; line-height: 1; letter-spacing: 1px;
  }
  .hours__title { font-size: 22px; font-weight: 600; line-height: 1; letter-spacing: 0.3px; }
  .hours__title span { display: block; }
  .hours__title span + span { letter-spacing: 4px; }
  .hours__rule { width: 2px; height: 50px; background: currentColor; margin: 0 3px; }
  .hours__times { font-size: 24px; font-weight: 600; line-height: 1.06; color: var(--blue); white-space: nowrap; }
  .banner--dark .hours__times { color: var(--white); }

  .header-rule {
    position: absolute; left: 30px; right: 18px; top: 100px;
    height: 2px; background: var(--navy);
  }
  .header-rule::after {
    content: ""; position: absolute; left: 50%; top: -1px;
    width: 250px; height: 4px; margin-left: -125px; background: var(--paper);
  }
  .brand-bar { position: absolute; left: 555px; top: 72px; width: 120px; margin-left: -105px; height: 4px; background: var(--red); }

  /* body */
  .messages {
    position: absolute; left: 30px; right: 20px; top: 114px;
    display: grid; grid-template-columns: 340px 360px 1fr; column-gap: 34px;
  }
  .banner--dark .messages { top: 106px; }
  .column { display: flex; flex-direction: column; gap: 13px; }

  .msg .tag { color: var(--white); padding: 0 3px; }
  .tag--blue { background: var(--blue); }
  .tag--red { background: var(--red); }
  .msg .accent-blue { color: var(--accent-blue); }
  .msg .accent-red { color: var(--accent-red); }

  .msg--en { font-family: "Oswald", sans-serif; font-weight: 600; font-size: 23px; line-height: 1.22; }
  .msg--ro { font-family: "Oswald", sans-serif; font-weight: 600; font-size: 21px; line-height: 1.2; }
  .msg--fr { font-family: "Roboto Condensed", sans-serif; font-style: italic; font-weight: 700; font-size: 23px; line-height: 1.24; }
  .msg--de, .msg--pl { font-family: "Raleway", sans-serif; font-weight: 500; font-size: 18px; line-height: 1.18; }
  .msg--nl { font-family: "Raleway", sans-serif; font-style: italic; font-weight: 600; font-size: 18px; line-height: 1.18; }
</style>
</head>
<body>

<section class="banner banner--light" aria-label="Ticket validation banner, light version">
  <header class="banner__header">
    <div class="steps" aria-label="Truck, ticket, shop, validated">
      <svg width="58" height="40" viewBox="0 0 58 40" fill="currentColor"><rect x="0" y="4" width="32" height="24" rx="2"/><path d="M35 12h10l8 9v9h-18z"/><circle cx="10" cy="33" r="5"/><circle cx="44" cy="33" r="5"/></svg>
      <svg width="26" height="20" viewBox="0 0 26 20" fill="none" stroke="currentColor" stroke-width="3.5"><path d="M2 10h20M14 2l8 8-8 8"/></svg>
      <svg width="56" height="36" viewBox="0 0 56 36"><path d="M6 2h44a4 4 0 0 0 4 4v24a4 4 0 0 0-4 4H6a4 4 0 0 0-4-4V6a4 4 0 0 0 4-4z" fill="none" stroke="currentColor" stroke-width="3.5"/><text x="28" y="23" text-anchor="middle" font-family="Oswald, sans-serif" font-weight="700" font-size="13" fill="currentColor">TICKET</text></svg>
      <svg width="26" height="20" viewBox="0 0 26 20" fill="none" stroke="currentColor" stroke-width="3.5"><path d="M2 10h20M14 2l8 8-8 8"/></svg>
      <svg width="46" height="40" viewBox="0 0 46 40" fill="currentColor"><rect x="2" y="0" width="42" height="9"/><text x="23" y="7.5" text-anchor="middle" font-family="Oswald, sans-serif" font-size="8" fill="#f4f5f7">SHOP</text><path d="M2 12h42v28H28V24H18v16H2z"/></svg>
      <svg width="26" height="20" viewBox="0 0 26 20" fill="none" stroke="currentColor" stroke-width="3.5"><path d="M2 10h20M14 2l8 8-8 8"/></svg>
      <svg width="40" height="40" viewBox="0 0 40 40"><circle cx="20" cy="20" r="18" fill="currentColor"/><path d="M11 20l6 6 12-12" fill="none" stroke="#f4f5f7" stroke-width="4"/></svg>
    </div>
    <div class="brand">Haulport 41Ter</div>
    <div class="hours">
      <div class="hours__shop">SHOP</div>
      <div class="hours__title"><span>OPENING</span><span>HOURS</span></div>
      <div class="hours__rule"></div>
      <div class="hours__times">Mon - Fri: 05:30 - 22:00<br>Sat &amp; Sun: 08:00 - 22:00</div>
    </div>
  </header>
  <div class="header-rule"></div>
  <div class="brand-bar"></div>

  <div class="messages">
    <div class="column">
      <p class="msg msg--en" lang="en">Don't forget to validate your entry ticket in the shop - <span class="tag tag--blue">mandatory,</span> <span class="accent-blue">even for short stops!</span></p>
      <p class="msg msg--nl" lang="nl">Vergeet je ticket niet te valideren in de shop – <span class="tag tag--red">verplicht,</span> <span class="accent-red">ook bij kort parkeren!</span></p>
    </div>
    <div class="column">
      <p class="msg msg--fr" lang="fr">N'oubliez pas de valider votre ticket à la boutique - <span class="tag tag--red">obligatoire,</span> <span class="accent-red">même pour un court arrêt !</span></p>
      <p class="msg msg--pl" lang="pl">Nie zapomnij zatwierdzić biletu w sklepie - <span class="tag tag--blue">obowiązkowe,</span> <span class="accent-blue">nawet przy krótkim postoju!</span></p>
    </div>
    <div class="column">
      <p class="msg msg--de" lang="de">Vergessen Sie nicht, Ihr Einfahrticket im Shop zu entwerten – <span class="tag tag--blue">Pflicht,</span> <span class="accent-blue">auch bei kurzem Parken!</span></p>
      <p class="msg msg--ro" lang="ro">Nu uitați să validați biletul în magazin - <span class="tag tag--red">obligatoriu,</span> <span class="accent-red">chiar și pentru opriri scurte!</span></p>
    </div>
  </div>
</section>

<section class="banner banner--dark" aria-label="Ticket validation banner, dark version">
  <div class="header-tab header-tab--left"></div>
  <div class="header-tab header-tab--right"></div>
  <header class="banner__header">
    <div class="steps" aria-label="Truck, ticket, shop, validated">
      <svg width="58" height="40" viewBox="0 0 58 40" fill="currentColor"><rect x="0" y="4" width="32" height="24" rx="2"/><path d="M35 12h10l8 9v9h-18z"/><circle cx="10" cy="33" r="5"/><circle cx="44" cy="33" r="5"/></svg>
      <svg width="26" height="20" viewBox="0 0 26 20" fill="none" stroke="currentColor" stroke-width="3.5"><path d="M2 10h20M14 2l8 8-8 8"/></svg>
      <svg width="56" height="36" viewBox="0 0 56 36"><path d="M6 2h44a4 4 0 0 0 4 4v24a4 4 0 0 0-4 4H6a4 4 0 0 0-4-4V6a4 4 0 0 0 4-4z" fill="none" stroke="currentColor" stroke-width="3.5"/><text x="28" y="23" text-anchor="middle" font-family="Oswald, sans-serif" font-weight="700" font-size="13" fill="currentColor">TICKET</text></svg>
      <svg width="26" height="20" viewBox="0 0 26 20" fill="none" stroke="currentColor" stroke-width="3.5"><path d="M2 10h20M14 2l8 8-8 8"/></svg>
      <svg width="46" height="40" viewBox="0 0 46 40" fill="currentColor"><rect x="2" y="0" width="42" height="9"/><text x="23" y="7.5" text-anchor="middle" font-family="Oswald, sans-serif" font-size="8" fill="#2a87d2">SHOP</text><path d="M2 12h42v28H28V24H18v16H2z"/></svg>
      <svg width="26" height="20" viewBox="0 0 26 20" fill="none" stroke="currentColor" stroke-width="3.5"><path d="M2 10h20M14 2l8 8-8 8"/></svg>
      <svg width="40" height="40" viewBox="0 0 40 40"><circle cx="20" cy="20" r="18" fill="currentColor"/><path d="M11 20l6 6 12-12" fill="none" stroke="#2a87d2" stroke-width="4"/></svg>
    </div>
    <div class="brand">Haulport 41Ter</div>
    <div class="hours">
      <div class="hours__shop">SHOP</div>
      <div class="hours__title"><span>OPENING</span><span>HOURS</span></div>
      <div class="hours__rule"></div>
      <div class="hours__times">Mon - Fri: 05:30 - 22:00<br>Sat &amp; Sun: 08:00 - 22:00</div>
    </div>
  </header>
  <div class="brand-bar"></div>

  <div class="messages">
    <div class="column">
      <p class="msg msg--en" lang="en">Don't forget to validate your entry ticket in the shop - <span class="tag tag--blue">mandatory,</span> <span class="accent-blue">even for short stops!</span></p>
      <p class="msg msg--nl" lang="nl">Vergeet je ticket niet te valideren in de shop – <span class="tag tag--red">verplicht,</span> <span class="accent-red">ook bij kort parkeren!</span></p>
    </div>
    <div class="column">
      <p class="msg msg--fr" lang="fr">N'oubliez pas de valider votre ticket à la boutique - <span class="tag tag--red">obligatoire,</span> <span class="accent-red">même pour un court arrêt !</span></p>
      <p class="msg msg--pl" lang="pl">Nie zapomnij zatwierdzić biletu w sklepie - <span class="tag tag--blue">obowiązkowe</span>, <span class="accent-blue">nawet przy krótkim postoju!</span></p>
    </div>
    <div class="column">
      <p class="msg msg--de" lang="de">Vergessen Sie nicht, Ihr Einfahrticket im Shop zu entwerten – <span class="tag tag--blue">Pflicht,</span> <span class="accent-blue">auch bei kurzem Parken!</span></p>
      <p class="msg msg--ro" lang="ro">Nu uitați să validați biletul în magazin - <span class="tag tag--red">obligatoriu,</span> <span class="accent-red">chiar și pentru opriri scurte!</span></p>
    </div>
  </div>
</section>

</body>
</html>
```